Steadfast Carewell (02)

We're designing a website to sell Medicare Supplements. Attached is the content we want to say and general layout, but please use your best knowledge to make it better. This platform is intentionally simplistic because this is reaching an older demographic, so it should be very straightforward, attention-grabbing and extremely user-friendly, while still appearing reliable and professional.
This should be a two-page web design. The homepage has information on Medicare supplements (script in image attached below) along with a button to input zip code. This triggers a window to pop up asking for personal information (will also be listed in attachment).
This brings you to the second page that lists out the medicare supplement companies and plans based on inputed information. We just want to see the design you have in mind, so it doesn't matter what information you put in this section. Feel free to reference/replicate the information in image 3 in the doc. There should be a section where you can filter results by company, premium price, or coverage plans.
Target Market(s)
Seniors, 65+
Industry/Entity Type
Insurance
Number of Pages Required
2 page
Look and feel

```html
<!DOCTYPE html>
<html lang="en">
<head>
<meta charset="utf-8">
<title>Steadfast Carewell — Home and Plans</title>
<link rel="stylesheet" href="https://fonts.googleapis.com/css2?family=Lato:wght@300;400;700;900&family=Montserrat:wght@300;400;700&display=swap">
<style>
:root{
  --canvas:#8f8b8e;
  --red:#e0312f;
  --ink:#23252b;
  --text:#3a3a3a;
  --muted:#6b6b6b;
  --line:#e3e3e3;
  --surface:#f2f2f2;
  --navy:#2c354b;
  --navy-deep:#1f2739;
  --white:#ffffff;
}
*{box-sizing:border-box;margin:0;padding:0}
html,body{width:1068px;height:1200px;overflow:hidden;background:var(--canvas)}
body{font-family:"Lato",sans-serif;color:var(--text);position:relative}
.stage{position:absolute;left:0;top:0;width:1820px;height:2044px;transform:scale(0.58681);transform-origin:0 0}
.page{position:absolute;top:90px;width:810px;height:1865px;background:var(--surface);overflow:hidden;box-shadow:0 4px 18px rgba(0,0,0,.25)}
.page--home{left:68px}
.page--plans{left:942px}
.abs{position:absolute}
.icon{display:inline-block;vertical-align:middle}

/* header */
.topbar{position:absolute;left:0;top:0;width:100%;height:58px;background:var(--white);border-top:3px solid var(--red)}
.brand{position:absolute;left:97px;top:9px;display:flex;align-items:center;gap:10px}
.brand-dot{width:40px;height:40px;border-radius:50%;background:var(--red)}
.brand-name{font-family:"Montserrat",sans-serif;font-weight:400;font-size:21px;color:var(--ink)}
.nav{position:absolute;left:385px;top:20px;font-size:11px;color:#555;display:flex;gap:14px}
.nav a{color:#555;text-decoration:none}
.nav .is-active{color:var(--ink);border-bottom:2px solid var(--red);padding-bottom:3px}
.head-call{position:absolute;left:527px;top:15px;display:flex;align-items:center;gap:6px;font-weight:900;font-size:17px;color:var(--ink)}

/* hero */
.hero{position:absolute;left:0;top:58px;width:100%;height:330px;background:linear-gradient(90deg,#f7f1ec 0%,#fbf8f4 100%)}
.hero-photo{position:absolute;left:0;top:0;width:440px;height:330px;background:linear-gradient(90deg,#8f6d7c 0%,#c9a7c6 35%,#e8dbe4 70%,rgba(250,246,242,0) 100%)}
.hero-title{position:absolute;left:389px;top:45px;font-family:"Montserrat",sans-serif;font-size:36px;line-height:43px;color:var(--ink)}
.hero-title b{font-weight:700;display:block}
.hero-title span{font-weight:300;display:block}
.hero-sub{position:absolute;left:389px;top:137px;width:320px;font-size:13px;line-height:18px;color:#666}
.hero-call{position:absolute;left:389px;top:193px;font-size:13px;color:#444;line-height:23px}
.hero-call .num{color:var(--red);font-weight:900;font-size:17px;margin:0 10px 0 4px}
.hero-call .line2{padding-left:33px}
.zip{position:absolute;left:389px;top:321px;width:270px;height:35px;background:var(--white);box-shadow:0 2px 6px rgba(0,0,0,.08)}
.zip-field{position:absolute;left:12px;top:12px;font-size:8.5px;color:#666;display:flex;gap:6px;align-items:center}
.zip-btn{position:absolute;left:152px;top:6px;width:117px;height:23px;background:var(--red);color:var(--white);font-weight:900;font-size:10.5px;display:flex;align-items:center;justify-content:center}

/* results */
.results{position:absolute;left:29px;top:428px;width:751px;height:1039px;background:var(--white);border:1px solid var(--line)}
.results-call{position:absolute;left:0;top:34px;width:100%;text-align:center;font-size:13px;color:#333}
.results-call .num{color:var(--red);font-weight:900;font-size:17px;margin:0 10px 0 4px}
.tab{position:absolute;top:89px;width:197px;height:88px;text-align:center;border:1px solid #d8d8d8;background:linear-gradient(#ffffff,#e9e9e9);padding-top:17px}
.tab h3{font-weight:400;font-size:13px;line-height:17px;color:#333}
.tab p{font-size:10px;color:var(--red);margin-top:7px}
.tab--active{background:linear-gradient(#3b3e48,#121318);border-color:#121318}
.tab--active h3{color:var(--white)}
.filter{position:absolute;left:54px;top:224px;width:148px;border:1px solid #d8d8d8;background:var(--white)}
.filter-row{height:57px;display:flex;align-items:center;gap:10px;padding-left:17px;font-size:12.5px;font-weight:700;color:var(--ink);border-bottom:1px solid #d8d8d8}
.filter-row:last-child{border-bottom:0}
.filter-row.is-active{background:#f4f4f4}
.filter-icon{width:26px;height:26px;background:var(--ink);display:flex;align-items:center;justify-content:center}
.filter-row.is-active .filter-icon{background:var(--red)}
.plan-list{position:absolute;left:216px;top:224px;width:510px;height:775px;border:1px solid var(--line);background:#fafafa}
.plan{position:absolute;left:21px;width:469px;height:233px;background:var(--white);box-shadow:0 1px 5px rgba(0,0,0,.08)}
.plan-side{position:absolute;left:0;top:0;width:154px;height:100%;border-right:1px solid #eee}
.price{position:absolute;left:30px;top:14px;font-weight:900;font-size:17px;color:var(--ink)}
.price-label{position:absolute;left:30px;top:40px;font-size:11px;color:#444}
.enroll{position:absolute;left:30px;top:71px;width:85px;height:24px;background:var(--red);color:var(--white);font-weight:900;font-size:9px;display:flex;align-items:center;justify-content:center}
.fav{position:absolute;left:30px;top:197px;font-size:9px;color:#444;display:flex;gap:5px;align-items:center}
.plan-main{position:absolute;left:195px;top:0;width:260px;height:100%}
.co-name{position:absolute;left:4px;top:22px;font-size:9px;font-weight:700;color:#4a6b3f;letter-spacing:.3px;text-transform:uppercase}
.plan-desc{position:absolute;left:0;top:56px;font-size:10.5px;color:#333}
.copay{position:absolute;top:81px;font-size:10px;color:#333}
.copay b{display:block;color:var(--red);font-weight:400;font-size:14px;margin-bottom:3px}
.feat-title{position:absolute;left:0;top:134px;font-weight:900;font-size:11.5px;color:var(--ink)}
.feats{position:absolute;top:157px;list-style:none;font-size:8.5px;color:#555;line-height:17px}
.feats li{display:flex;align-items:center;gap:4px}

/* footer */
.footer{position:absolute;left:0;top:1515px;width:100%;height:293px;background:var(--navy)}
.foot-ask{position:absolute;left:382px;top:35px;font-size:14px;font-weight:300;line-height:20px;color:#d9dce4}
.foot-call{position:absolute;left:527px;top:42px;display:flex;align-items:center;gap:6px;font-weight:900;font-size:17px;color:var(--white)}
.foot-col{position:absolute;top:101px}
.foot-col h4{font-weight:400;font-size:15px;color:var(--red);margin-bottom:12px}
.foot-col a{display:block;font-size:8.5px;color:#dfe2ea;text-decoration:none;line-height:20px}
.foot-cta{position:absolute;left:673px;top:217px;width:140px;height:38px;border-radius:19px 0 0 19px;background:var(--red);color:var(--white);font-size:11px;display:flex;align-items:center;justify-content:center}
.subfoot{position:absolute;left:0;top:1808px;width:100%;height:57px;background:var(--navy-deep)}
.copyright{position:absolute;left:97px;top:23px;font-size:8px;color:#cfd3dc}
.socials{position:absolute;left:603px;top:17px;display:flex;gap:8px}
.socials span{width:21px;height:21px;border-radius:50%;border:1px solid #cfd3dc}

/* quote dialog */
.dim{position:absolute;inset:0;background:rgba(120,118,120,.55)}
.dialog{position:absolute;left:93px;top:391px;width:623px;height:663px;background:var(--white);box-shadow:0 6px 24px rgba(0,0,0,.3);font-size:10px;color:#333}
.dialog-close{position:absolute;left:589px;top:-1px;width:35px;height:35px;border-radius:50%;background:var(--red);display:flex;align-items:center;justify-content:center}
.dialog h2{position:absolute;left:67px;top:40px;font-size:22px;font-weight:900;color:var(--ink)}
.dialog-rule{position:absolute;left:67px;top:81px;width:46px;height:2px;background:var(--red)}
.dialog-intro{position:absolute;left:67px;top:108px;width:490px;font-size:10px;line-height:20px;color:#555}
.lbl{position:absolute;font-size:10px;color:#333}
.lbl-strong{position:absolute;font-size:11px;color:#222}
.radio{position:absolute;top:240px;display:flex;align-items:center;gap:5px;font-size:10px;color:#444}
.radio i{width:9px;height:9px;border-radius:50%;border:1.5px solid #555;display:block}
.field{position:absolute;height:28px;border:1px solid #bbb;font-size:8.5px;color:#555;display:flex;align-items:center;padding-left:10px;gap:5px}
.select::after{content:"";position:absolute;right:14px;top:12px;border-left:3px solid transparent;border-right:3px solid transparent;border-top:4px solid #333}
.btn-primary{position:absolute;left:85px;top:591px;width:84px;height:27px;background:var(--red);color:var(--white);font-weight:900;font-size:8px;display:flex;align-items:center;justify-content:center}
.btn-ghost{position:absolute;left:176px;top:591px;width:101px;height:27px;border:1px solid #999;color:var(--red);font-size:8px;display:flex;align-items:center;justify-content:center}
</style>
</head>
<body>
<svg width="0" height="0" style="position:absolute" aria-hidden="true">
  <symbol id="i-phone" viewBox="0 0 24 24"><circle cx="12" cy="12" r="10.5" fill="none" stroke="#e0312f" stroke-width="1.5"/><path d="M8.2 6.5l2 2.2-1 1.6c.8 1.8 2.1 3.2 3.9 4l1.6-1 2.2 2-1.1 1.9c-4 .2-8.6-4.3-8.5-8.6z" fill="#e0312f"/></symbol>
  <symbol id="i-pin" viewBox="0 0 12 12"><path d="M6 1a3.5 3.5 0 0 0-3.5 3.5C2.5 7 6 11 6 11s3.5-4 3.5-6.5A3.5 3.5 0 0 0 6 1zm0 4.8a1.3 1.3 0 1 1 0-2.6 1.3 1.3 0 0 1 0 2.6z" fill="#e0312f"/></symbol>
  <symbol id="i-tick" viewBox="0 0 10 10"><path d="M1.5 5.2l2.3 2.3L8.6 2.6" fill="none" stroke="#e0312f" stroke-width="1.8"/></symbol>
  <symbol id="i-heart" viewBox="0 0 12 12"><path d="M6 10.5S1 7.3 1 4.2A2.5 2.5 0 0 1 6 3a2.5 2.5 0 0 1 5 1.2c0 3.1-5 6.3-5 6.3z" fill="#e0312f"/></symbol>
  <symbol id="i-cal" viewBox="0 0 10 10"><rect x="1" y="2" width="8" height="7" fill="none" stroke="#e0312f"/><path d="M1 4h8M3 1v2M7 1v2" stroke="#e0312f"/></symbol>
</svg>

<div class="stage">

<!-- ============ HOME PAGE WITH QUOTE DIALOG ============ -->
<section class="page page--home">
  <header class="topbar">
    <div class="brand"><span class="brand-dot"></span><span class="brand-name">Steadfast Carewell</span></div>
    <nav class="nav"><a class="is-active">Home</a><a>Quote</a><a>Blog</a></nav>
    <div class="head-call"><svg class="icon" width="24" height="24"><use href="#i-phone"/></svg>CALL (800) 555-0142</div>
  </header>
  <div class="hero">
    <div class="hero-photo" role="img" aria-label="Photo of a smiling senior woman in a striped top, seated outdoors"></div>
    <h1 class="hero-title"><b>STEADFAST</b><span>CAREWELL</span></h1>
    <p class="hero-sub">Be confident in choosing the Medicare Supplement plan that’s right for you.</p>
    <div class="hero-call"><svg class="icon" width="24" height="24"><use href="#i-phone"/></svg><span class="num">CALL (800) 555-0142</span>for more information,<div class="line2">or continue to view our premium plans below</div></div>
    <div class="zip"><div class="zip-field"><svg width="10" height="10"><use href="#i-pin"/></svg>Enter Zipcode</div><div class="zip-btn">GET FREE QUOTE</div></div>
  </div>
  <main class="results">
    <div class="results-call"><svg class="icon" width="24" height="24"><use href="#i-phone"/></svg><span class="num">CALL (800) 555-0142</span>for more information,or continue to view our premium plans below</div>
    <div class="tab tab--active" style="left:54px"><h3>Medicare<br>Advantage Plans</h3><p>3 Plans Available</p></div>
    <div class="tab" style="left:276px"><h3>Medicare Supplement<br>Insurance Plans</h3><p>21 Plans Available</p></div>
    <div class="tab" style="left:498px"><h3>Medicare<br>Part D Plans</h3><p>23 Plans Available</p></div>
    <div class="filter">
      <div class="filter-row is-active"><span class="filter-icon"><svg width="12" height="12" viewBox="0 0 12 12"><circle cx="6" cy="3.5" r="2.3" fill="#fff"/><path d="M1.5 11c0-3 2-4.5 4.5-4.5s4.5 1.5 4.5 4.5z" fill="#fff"/></svg></span>Company</div>
      <div class="filter-row"><span class="filter-icon"><svg width="12" height="14" viewBox="0 0 12 14"><text x="6" y="12" text-anchor="middle" font-family="Lato,sans-serif" font-weight="900" font-size="13" fill="#fff">$</text></svg></span>Premium price</div>
      <div class="filter-row"><span class="filter-icon"><svg width="12" height="10" viewBox="0 0 12 10"><path d="M0 1h2M4 1h8M0 5h2M4 5h8M0 9h2M4 9h8" stroke="#fff" stroke-width="1.8"/></svg></span>Plan type</div>
    </div>
    <div class="plan-list">
      <article class="plan" style="top:21px">
        <div class="plan-side"><div class="price">$56.89</div><div class="price-label">Monthly Premium</div><div class="enroll">ENROLL NOW</div><div class="fav"><svg width="10" height="10"><use href="#i-heart"/></svg>Add to favourites</div></div>
        <div class="plan-main"><div class="co-name">Company Name</div><div class="plan-desc">Lorem ipsum dolor sit amet</div><div class="copay" style="left:0"><b>$5</b>Primary Doctor Co-Pay</div><div class="copay" style="left:135px"><b>$15</b>Specialist Co-Pay</div><div class="feat-title">PLAN FEATURES</div>
        <ul class="feats" style="left:0"><li><svg width="9" height="9"><use href="#i-tick"/></svg>Lorem ipsum dolor sit</li><li><svg width="9" height="9"><use href="#i-tick"/></svg>Ullamco laboris nisi</li><li><svg width="9" height="9"><use href="#i-tick"/></svg>Excepteur sint occaeca</li></ul>
        <ul class="feats" style="left:135px"><li><svg width="9" height="9"><use href="#i-tick"/></svg>Excepteur sint</li><li><svg width="9" height="9"><use href="#i-tick"/></svg>Duis aute irure</li><li><svg width="9" height="9"><use href="#i-tick"/></svg>Et in culpa qui offici</li></ul></div>
      </article>
      <article class="plan" style="top:269px">
        <div class="plan-side"><div class="price">$56.89</div><div class="price-label">Monthly Premium</div><div class="enroll">ENROLL NOW</div><div class="fav"><svg width="10" height="10"><use href="#i-heart"/></svg>Add to favourites</div></div>
        <div class="plan-main"><div class="co-name">Company Name</div><div class="plan-desc">Lorem ipsum dolor sit amet</div><div class="copay" style="left:0"><b>$5</b>Primary Doctor Co-Pay</div><div class="copay" style="left:135px"><b>$15</b>Specialist Co-Pay</div><div class="feat-title">PLAN FEATURES</div>
        <ul class="feats" style="left:0"><li><svg width="9" height="9"><use href="#i-tick"/></svg>Lorem ipsum dolor sit</li><li><svg width="9" height="9"><use href="#i-tick"/></svg>Ullamco laboris nisi</li><li><svg width="9" height="9"><use href="#i-tick"/></svg>Excepteur sint occaeca</li></ul>
        <ul class="feats" style="left:135px"><li><svg width="9" height="9"><use href="#i-tick"/></svg>Excepteur sint</li><li><svg width="9" height="9"><use href="#i-tick"/></svg>Duis aute irure</li><li><svg width="9" height="9"><use href="#i-tick"/></svg>Et in culpa qui offici</li></ul></div>
      </article>
      <article class="plan" style="top:517px">
        <div class="plan-side"><div class="price">$56.89</div><div class="price-label">Monthly Premium</div><div class="enroll">ENROLL NOW</div><div class="fav"><svg width="10" height="10"><use href="#i-heart"/></svg>Add to favourites</div></div>
        <div class="plan-main"><div class="co-name">Company Name</div><div class="plan-desc">Lorem ipsum dolor sit amet</div><div class="copay" style="left:0"><b>$5</b>Primary Doctor Co-Pay</div><div class="copay" style="left:135px"><b>$15</b>Specialist Co-Pay</div><div class="feat-title">PLAN FEATURES</div>
        <ul class="feats" style="left:0"><li><svg width="9" height="9"><use href="#i-tick"/></svg>Lorem ipsum dolor sit</li><li><svg width="9" height="9"><use href="#i-tick"/></svg>Ullamco laboris nisi</li><li><svg width="9" height="9"><use href="#i-tick"/></svg>Excepteur sint occaeca</li></ul>
        <ul class="feats" style="left:135px"><li><svg width="9" height="9"><use href="#i-tick"/></svg>Excepteur sint</li><li><svg width="9" height="9"><use href="#i-tick"/></svg>Duis aute irure</li><li><svg width="9" height="9"><use href="#i-tick"/></svg>Et in culpa qui offici</li></ul></div>
      </article>
    </div>
  </main>
  <footer class="footer">
    <p class="foot-ask">Questions?<br>Speak with an Expert</p>
    <div class="foot-call"><svg class="icon" width="24" height="24"><use href="#i-phone"/></svg>CALL (800) 555-0142</div>
    <div class="foot-col" style="left:382px"><h4>SITEMAP</h4><a>HOME</a><a>ABOUT US</a><a>BLOG</a><a>MEDICARE PLANS</a><a>CONTACT US</a><a>AFFILIATE PROGRAM</a></div>
    <div class="foot-col" style="left:544px"><h4>INSURANCE QUOTES</h4><a>HEALTH INSURANCE</a><a>LIFE INSURANCE</a><a>FINAL EXPENSE INSURANCE</a></div>
    <div class="foot-cta">GET FREE QUOTES</div>
  </footer>
  <div class="subfoot"><p class="copyright">Copyright © 2020 Steadfast Carewell. All rights reserved &nbsp;|&nbsp; Privacy Policy &nbsp;|&nbsp; Terms and Use</p><div class="socials"><span></span><span></span><span></span><span></span></div></div>

  <div class="dim"></div>
  <div class="dialog" role="dialog" aria-label="Get A Quote">
    <div class="dialog-close"><svg width="10" height="10" viewBox="0 0 10 10"><path d="M1.5 1.5l7 7M8.5 1.5l-7 7" stroke="#fff" stroke-width="2"/></svg></div>
    <h2>Get A Quote</h2>
    <div class="dialog-rule"></div>
    <p class="dialog-intro">Lorem ipsum dolor sit amet, consectetur adipiscing elit, sed do eiusmod tempor incididunt ut magna aliqua spendisse ultrices gravida. Risus commodo viverra maecenas accumsan lacus vel facilisis. Lorem ipsum dolor sit amet, consectetur adipiscing elit, sed do eiusmod tempor incididunt ut magna aliqua</p>
    <span class="lbl" style="left:67px;top:201px">Gender *</span>
    <span class="lbl" style="left:208px;top:201px">Age *</span>
    <span class="lbl" style="left:327px;top:201px">Date of Birth *</span>
    <div class="radio" style="left:67px"><i></i>Male</div>
    <div class="radio" style="left:119px"><i></i>Female</div>
    <div class="field" style="left:208px;top:222px;width:85px">Years</div>
    <div class="field" style="left:327px;top:222px;width:158px"><svg width="9" height="9"><use href="#i-cal"/></svg>MM/DD/YY</div>
    <span class="lbl" style="left:67px;top:287px">Hospital Insurnace (Part A) *</span>
    <span class="lbl-strong" style="left:67px;top:315px">Part A Month</span>
    <span class="lbl-strong" style="left:238px;top:315px">Part A Month</span>
    <div class="field select" style="left:67px;top:337px;width:200px">Month</div>
    <div class="field select" style="left:285px;top:337px;width:200px">Year</div>
    <span class="lbl" style="left:67px;top:401px">Medical Insurance (Part B) *</span>
    <span class="lbl-strong" style="left:67px;top:429px">Part B Month</span>
    <span class="lbl-strong" style="left:284px;top:429px">Part B Year</span>
    <div class="field select" style="left:67px;top:451px;width:200px">Month</div>
    <div class="field select" style="left:285px;top:451px;width:200px">Year</div>
    <span class="lbl" style="left:67px;top:508px">Desired Coverage Start Date *</span>
    <div class="field" style="left:67px;top:529px;width:418px"><svg width="9" height="9"><use href="#i-cal"/></svg>MM/DD/YY</div>
    <div class="btn-primary">COMPARE RATES</div>
    <div class="btn-ghost">CANCEL</div>
  </div>
</section>

<!-- ============ PLANS PAGE ============ -->
<section class="page page--plans">
  <header class="topbar">
    <div class="brand"><span class="brand-dot"></span><span class="brand-name">Steadfast Carewell</span></div>
    <nav class="nav"><a class="is-active">Home</a><a>Quote</a><a>Blog</a></nav>
    <div class="head-call"><svg class="icon" width="24" height="24"><use href="#i-phone"/></svg>CALL (800) 555-0142</div>
  </header>
  <div class="hero">
    <div class="hero-photo" role="img" aria-label="Photo of a smiling senior woman in a striped top, seated outdoors"></div>
    <h1 class="hero-title"><b>STEADFAST</b><span>CAREWELL</span></h1>
    <p class="hero-sub">Be confident in choosing the Medicare Supplement plan that’s right for you.</p>
    <div class="hero-call"><svg class="icon" width="24" height="24"><use href="#i-phone"/></svg><span class="num">CALL (800) 555-0142</span>for more information,<div class="line2">or continue to view our premium plans below</div></div>
    <div class="zip"><div class="zip-field"><svg width="10" height="10"><use href="#i-pin"/></svg>Enter Zipcode</div><div class="zip-btn">GET FREE QUOTE</div></div>
  </div>
  <main class="results">
    <div class="results-call"><svg class="icon" width="24" height="24"><use href="#i-phone"/></svg><span class="num">CALL (800) 555-0142</span>for more information,or continue to view our premium plans below</div>
    <div class="tab tab--active" style="left:54px"><h3>Medicare<br>Advantage Plans</h3><p>3 Plans Available</p></div>
    <div class="tab" style="left:276px"><h3>Medicare Supplement<br>Insurance Plans</h3><p>21 Plans Available</p></div>
    <div class="tab" style="left:498px"><h3>Medicare<br>Part D Plans</h3><p>23 Plans Available</p></div>
    <div class="filter">
      <div class="filter-row is-active"><span class="filter-icon"><svg width="12" height="12" viewBox="0 0 12 12"><circle cx="6" cy="3.5" r="2.3" fill="#fff"/><path d="M1.5 11c0-3 2-4.5 4.5-4.5s4.5 1.5 4.5 4.5z" fill="#fff"/></svg></span>Company</div>
      <div class="filter-row"><span class="filter-icon"><svg width="12" height="14" viewBox="0 0 12 14"><text x="6" y="12" text-anchor="middle" font-family="Lato,sans-serif" font-weight="900" font-size="13" fill="#fff">$</text></svg></span>Premium price</div>
      <div class="filter-row"><span class="filter-icon"><svg width="12" height="10" viewBox="0 0 12 10"><path d="M0 1h2M4 1h8M0 5h2M4 5h8M0 9h2M4 9h8" stroke="#fff" stroke-width="1.8"/></svg></span>Plan type</div>
    </div>
    <div class="plan-list">
      <article class="plan" style="top:21px">
        <div class="plan-side"><div class="price">$56.89</div><div class="price-label">Monthly Premium</div><div class="enroll">ENROLL NOW</div><div class="fav"><svg width="10" height="10"><use href="#i-heart"/></svg>Add to favourites</div></div>
        <div class="plan-main"><div class="co-name">Company Name</div><div class="plan-desc">Lorem ipsum dolor sit amet</div><div class="copay" style="left:0"><b>$5</b>Primary Doctor Co-Pay</div><div class="copay" style="left:135px"><b>$15</b>Specialist Co-Pay</div><div class="feat-title">PLAN FEATURES</div>
        <ul class="feats" style="left:0"><li><svg width="9" height="9"><use href="#i-tick"/></svg>Lorem ipsum dolor sit</li><li><svg width="9" height="9"><use href="#i-tick"/></svg>Ullamco laboris nisi</li><li><svg width="9" height="9"><use href="#i-tick"/></svg>Excepteur sint occaeca</li></ul>
        <ul class="feats" style="left:135px"><li><svg width="9" height="9"><use href="#i-tick"/></svg>Excepteur sint</li><li><svg width="9" height="9"><use href="#i-tick"/></svg>Duis aute irure</li><li><svg width="9" height="9"><use href="#i-tick"/></svg>Et in culpa qui offici</li></ul></div>
      </article>
      <article class="plan" style="top:269px">
        <div class="plan-side"><div class="price">$56.89</div><div class="price-label">Monthly Premium</div><div class="enroll">ENROLL NOW</div><div class="fav"><svg width="10" height="10"><use href="#i-heart"/></svg>Add to favourites</div></div>
        <div class="plan-main"><div class="co-name" style="color:#555">Company Name</div><div class="plan-desc">Lorem ipsum dolor sit amet</div><div class="copay" style="left:0"><b>$5</b>Primary Doctor Co-Pay</div><div class="copay" style="left:135px"><b>$15</b>Specialist Co-Pay</div><div class="feat-title">PLAN FEATURES</div>
        <ul class="feats" style="left:0"><li><svg width="9" height="9"><use href="#i-tick"/></svg>Lorem ipsum dolor sit</li><li><svg width="9" height="9"><use href="#i-tick"/></svg>Ullamco laboris nisi</li><li><svg width="9" height="9"><use href="#i-tick"/></svg>Excepteur sint occaeca</li></ul>
        <ul class="feats" style="left:135px"><li><svg width="9" height="9"><use href="#i-tick"/></svg>Excepteur sint</li><li><svg width="9" height="9"><use href="#i-tick"/></svg>Duis aute irure</li><li><svg width="9" height="9"><use href="#i-tick"/></svg>Et in culpa qui offici</li></ul></div>
      </article>
      <article class="plan" style="top:517px">
        <div class="plan-side"><div class="price">$56.89</div><div class="price-label">Monthly Premium</div><div class="enroll">ENROLL NOW</div><div class="fav"><svg width="10" height="10"><use href="#i-heart"/></svg>Add to favourites</div></div>
        <div class="plan-main"><div class="co-name" style="color:#555">Company Name</div><div class="plan-desc">Lorem ipsum dolor sit amet</div><div class="copay" style="left:0"><b>$5</b>Primary Doctor Co-Pay</div><div class="copay" style="left:135px"><b>$15</b>Specialist Co-Pay</div><div class="feat-title">PLAN FEATURES</div>
        <ul class="feats" style="left:0"><li><svg width="9" height="9"><use href="#i-tick"/></svg>Lorem ipsum dolor sit</li><li><svg width="9" height="9"><use href="#i-tick"/></svg>Ullamco laboris nisi</li><li><svg width="9" height="9"><use href="#i-tick"/></svg>Excepteur sint occaeca</li></ul>
        <ul class="feats" style="left:135px"><li><svg width="9" height="9"><use href="#i-tick"/></svg>Excepteur sint</li><li><svg width="9" height="9"><use href="#i-tick"/></svg>Duis aute irure</li><li><svg width="9" height="9"><use href="#i-tick"/></svg>Et in culpa qui offici</li></ul></div>
      </article>
    </div>
  </main>
  <footer class="footer">
    <p class="foot-ask">Questions?<br>Speak with an Expert</p>
    <div class="foot-call"><svg class="icon" width="24" height="24"><use href="#i-phone"/></svg>CALL (800) 555-0142</div>
    <div class="foot-col" style="left:382px"><h4>SITEMAP</h4><a>HOME</a><a>ABOUT US</a><a>BLOG</a><a>MEDICARE PLANS</a><a>CONTACT US</a><a>AFFILIATE PROGRAM</a></div>
    <div class="foot-col" style="left:544px"><h4>INSURANCE QUOTES</h4><a>HEALTH INSURANCE</a><a>LIFE INSURANCE</a><a>FINAL EXPENSE INSURANCE</a></div>
    <div class="foot-cta">GET FREE QUOTES</div>
  </footer>
  <div class="subfoot"><p class="copyright">Copyright © 2020 Steadfast Carewell. All rights reserved &nbsp;|&nbsp; Privacy Policy &nbsp;|&nbsp; Terms and Use</p><div class="socials"><span></span><span></span><span></span><span></span></div></div>
</section>

</div>
</body>
</html>
```